Web Design Project

We have screen protector brand for mobile phone and we need
Looking for talented web designer. We need only graphic design of 3 page design Home, Catalog page and Product page

- Home page
- There will be rotating banners on the home page
- Top menu will have Hot products, Screen Protectors, Videos, Contact us
- Screen Protectors will be submenu
- Website will be two languages so put US and Turkish flags on the corner so users will be able to switch
- Home page, there will be newest products and hot products and also one video

I also live any additional creative idea for the website
There will be one inner page and catalog page

Check existing page www.durvelo.com which looks pretty bad. You can take logo from there. If you need logo separate i can send it.

I have attached the layout but feel free to change it. I only try to give idea what i wanna see on it.

```html
<!DOCTYPE html>
<html lang="en">
<head>
<meta charset="utf-8">
<title>Durvelo – Screen Protectors</title>
<link href="https://fonts.googleapis.com/css2?family=Arimo:wght@400;700&display=swap" rel="stylesheet">
<style>
  :root {
    --orange: #e24a00;
    --dark: #2f363d;
    --black: #050607;
    --text: #333;
    --muted: #d8dde2;
    --page: #fff;
    --footer-bg: #f6f6f6;
    --line: #dcdcdc;
    --flag-red: #c8102e;
    --flag-blue: #2a3a7a;
  }
  * { box-sizing: border-box; margin: 0; padding: 0; }
  html, body { width: 1098px; height: 1200px; overflow: hidden; background: var(--page); }
  body { font-family: "Arimo", Arial, sans-serif; color: var(--text); position: relative; }
  .abs { position: absolute; }

  .site-header { left: 0; top: 0; width: 1098px; height: 73px; background: linear-gradient(#fff, #f3f4f6); border-bottom: 1px solid var(--line); }
  .brand { left: 112px; top: 28px; display: flex; align-items: center; gap: 8px; font-size: 30px; font-weight: 700; color: #3b4046; letter-spacing: 1px; }
  .brand-mark { width: 16px; height: 16px; background: var(--orange); }
  .language-switch { left: 818px; top: 16px; display: flex; gap: 5px; }
  .language-switch svg { display: block; box-shadow: 0 0 0 1px #ccc; }
  .top-links { left: 872px; top: 17px; font-size: 11px; color: #444; }
  .top-links span { margin: 0 9px; }
  .search-input { left: 611px; top: 36px; width: 277px; height: 19px; border: 1px solid #c9c9c9; background: #fff; }
  .search-btn { left: 895px; top: 37px; width: 110px; height: 17px; background: var(--orange); color: #fff; font-size: 10px; font-weight: 700; text-align: center; line-height: 17px; }

  .main-nav { left: 92px; top: 77px; width: 914px; height: 36px; background: linear-gradient(#4a535b, #2f363c); border-radius: 3px; display: flex; }
  .main-nav a { color: #fff; text-decoration: none; font-size: 11.5px; font-weight: 700; display: flex; align-items: center; justify-content: center; border-right: 1px solid #252b30; }
  .main-nav a:last-child { border-right: 0; }

  .hero { left: 92px; top: 116px; width: 914px; height: 346px; background: var(--black); border-radius: 3px; overflow: hidden; }
  .hero-backdrop { left: 0; top: 0; width: 520px; height: 346px; background: radial-gradient(ellipse at 35% 60%, #2c384a 0%, #121821 55%, #050607 100%); }
  .hero-phone { width: 92px; height: 310px; border-radius: 14px; }
  .hero-phone.light { left: 74px; top: 6px; background: linear-gradient(160deg, #e4e7ea, #9aa3ab 40%, #3f6a9a 55%, #6a7b8c); }
  .hero-phone.dark { left: 160px; top: 18px; background: linear-gradient(160deg, #2a2d31, #3d5f8c 45%, #5a86b8 60%, #15181c); }
  .hero-title { left: 513px; top: 52px; font-size: 51px; font-weight: 700; color: #fff; letter-spacing: 2px; }
  .hero-text { left: 519px; top: 117px; width: 350px; font-size: 20px; font-weight: 700; line-height: 31px; color: #fff; }
  .hero-dots { left: 818px; top: 326px; display: flex; gap: 9px; }
  .hero-dots i { width: 8px; height: 8px; border-radius: 50%; background: #3b4a5e; }

  .new-products { left: 92px; top: 467px; width: 914px; height: 177px; background: var(--orange); border-radius: 3px; }
  .section-title { font-size: 15px; font-weight: 700; color: #fff; }
  .new-products .section-title { left: 19px; top: 9px; }
  .product-thumb { top: 35px; width: 126px; height: 126px; background: #fff; }
  .product-thumb div { position: absolute; left: 30px; top: 6px; width: 66px; height: 114px; border-radius: 8px; background: linear-gradient(#5a5f66, #1d2024); }

  .video-panel { left: 92px; top: 651px; width: 318px; height: 236px; background: var(--dark); border-radius: 3px; overflow: hidden; }
  .video-panel .section-title { left: 19px; top: 6px; font-size: 16px; }
  .video-frame { left: 0; top: 31px; width: 318px; height: 182px; background: var(--black); }
  .video-still { left: 33px; top: 0; width: 245px; height: 182px; background: linear-gradient(135deg, #8d8a84, #c9c5bd 55%, #a29e96); }
  .play { left: 140px; top: 64px; }
  .video-controls { left: 0; top: 213px; width: 318px; height: 23px; background: #1b1f23; }

  .features { left: 422px; top: 651px; width: 584px; height: 236px; background: var(--dark); border-radius: 3px; }
  .feature { left: 14px; width: 556px; height: 74px; }
  .feature + .feature { border-top: 1px solid #4a535b; }
  .feature-icon { left: 4px; width: 76px; height: 60px; }
  .feature h3 { position: absolute; left: 96px; font-size: 13px; font-weight: 700; color: var(--orange); }
  .feature p { position: absolute; left: 96px; width: 450px; font-size: 11px; line-height: 16px; color: var(--muted); }

  .footer-links { left: 0; top: 915px; width: 1098px; height: 239px; background: linear-gradient(#eeeeee, var(--footer-bg) 30px); border-top: 1px solid var(--line); }
  .link-col { top: 14px; }
  .link-col h4 { font-size: 12px; font-weight: 700; color: var(--orange); margin-bottom: 9px; }
  .link-col li { list-style: none; font-size: 11.5px; line-height: 23px; color: #333; }
  .site-footer { left: 0; top: 1154px; width: 1098px; height: 46px; background: #fafafa; border-top: 1px solid var(--line); }
  .copyright { left: 93px; top: 17px; font-size: 11px; }
  .follow { left: 835px; top: 11px; display: flex; align-items: center; gap: 5px; font-size: 11.5px; }
  .follow i { width: 21px; height: 21px; border-radius: 3px; background: #7b8794; }
</style>
</head>
<body>
  <header class="site-header abs">
    <div class="brand abs"><span class="brand-mark"></span>DURVELO</div>
    <div class="language-switch abs" aria-label="Language">
      <svg width="20" height="13" viewBox="0 0 20 13" role="img" aria-label="English">
        <rect width="20" height="13" fill="#fff"/>
        <rect y="0" width="20" height="1.86" fill="var(--flag-red)"/>
        <rect y="3.71" width="20" height="1.86" fill="var(--flag-red)"/>
        <rect y="7.43" width="20" height="1.86" fill="var(--flag-red)"/>
        <rect y="11.14" width="20" height="1.86" fill="var(--flag-red)"/>
        <rect width="9" height="7" fill="var(--flag-blue)"/>
      </svg>
      <svg width="20" height="13" viewBox="0 0 20 13" role="img" aria-label="Türkçe">
        <rect width="20" height="13" fill="var(--flag-red)"/>
        <circle cx="8" cy="6.5" r="3.6" fill="#fff"/>
        <circle cx="9" cy="6.5" r="2.9" fill="var(--flag-red)"/>
        <circle cx="13" cy="6.5" r="1.2" fill="#fff"/>
      </svg>
    </div>
    <nav class="top-links abs">HOME<span>|</span>CONTACT US</nav>
    <div class="search-input abs"></div>
    <div class="search-btn abs">SEARCH</div>
  </header>

  <nav class="main-nav abs">
    <a style="width:203px">HOT OFFERS</a>
    <a style="width:238px">SCREEN PROTECTORS</a>
    <a style="width:236px">VIDEOS</a>
    <a style="width:237px">CONTACT US</a>
  </nav>

  <section class="hero abs">
    <div class="hero-backdrop abs"></div>
    <div class="hero-phone light abs" role="img" aria-label="White smartphone shown front-on"></div>
    <div class="hero-phone dark abs" role="img" aria-label="Black smartphone shown front-on"></div>
    <h1 class="hero-title abs">PROTECT</h1>
    <p class="hero-text abs">Get the award winning protection of the clearguard, the orginal and industry</p>
    <div class="hero-dots abs"><i></i><i></i><i></i><i></i><i></i></div>
  </section>

  <section class="new-products abs">
    <h2 class="section-title abs">NEW PRODUCTS</h2>
    <div class="product-thumb abs" style="left:20px" role="img" aria-label="Smartphone with screen protector"><div></div></div>
    <div class="product-thumb abs" style="left:170px" role="img" aria-label="Smartphone with screen protector"><div></div></div>
    <div class="product-thumb abs" style="left:320px" role="img" aria-label="Keyboard phone with screen protector"><div></div></div>
    <div class="product-thumb abs" style="left:471px" role="img" aria-label="Keyboard phone with screen protector"><div></div></div>
    <div class="product-thumb abs" style="left:621px" role="img" aria-label="Compact smartphone with screen protector"><div></div></div>
    <div class="product-thumb abs" style="left:771px" role="img" aria-label="Large smartphone with screen protector"><div></div></div>
  </section>

  <section class="video-panel abs">
    <h2 class="section-title abs">VIDEO</h2>
    <div class="video-frame abs">
      <div class="video-still abs" role="img" aria-label="Video still of a hand holding a phone"></div>
      <svg class="play abs" width="44" height="50" viewBox="0 0 44 50"><polygon points="2,2 42,25 2,48" fill="#5b5f63" opacity="0.85"/></svg>
    </div>
    <div class="video-controls abs">
      <svg width="318" height="23"><rect x="7" y="7" width="2" height="8" fill="#aaa"/><rect x="11" y="7" width="2" height="8" fill="#aaa"/><rect x="0" y="0" width="18" height="2" fill="#ccc"/><circle cx="290" cy="11" r="3" fill="#888"/><rect x="300" y="8" width="8" height="6" fill="none" stroke="#aaa"/></svg>
    </div>
  </section>

  <section class="features abs">
    <div class="feature abs" style="top:8px">
      <div class="feature-icon abs" style="top:2px;background:linear-gradient(90deg,transparent 25px,#7c848c 25px,#3b4046 52px,transparent 52px)" role="img" aria-label="Phone with protective film"></div>
      <h3 style="top:6px">ANTI SCRATCH</h3>
      <p style="top:27px">Ted ut perspiciatis unde omnis iste natus error sit voluptatem accusantium doloremque laudantium, totam rem iste natus error</p>
    </div>
    <div class="feature abs" style="top:76px;height:74px">
      <div class="feature-icon abs" style="top:8px;background:radial-gradient(ellipse,#c9825a 0%,#8a4b2e 55%,transparent 70%)" role="img" aria-label="Fingerprint"></div>
      <h3 style="top:16px">ANTI FINGER PRINT</h3>
      <p style="top:37px">Ted ut perspiciatis unde omnis iste natus error sit voluptatem accusantium doloremque laudantium, totam rem iste natus error</p>
    </div>
    <div class="feature abs" style="top:150px;height:80px">
      <div class="feature-icon abs" style="top:8px;background:linear-gradient(90deg,transparent 18px,#9aa1a8 18px,#1e2227 56px,transparent 56px)" role="img" aria-label="Two phones with screen film"></div>
      <h3 style="top:20px">WASHABLE</h3>
      <p style="top:41px">Ted ut perspiciatis unde omnis iste natus error sit voluptatem accusantium doloremque laudantium, totam rem iste natus error</p>
    </div>
  </section>

  <section class="footer-links abs">
    <div class="link-col abs" style="left:93px"><h4>Lorum Ipsum</h4><ul><li>Ted ut perspiciatis unde omnis</li><li>Ted ut perspiciatis unde omnis</li><li>Ted ut perspiciatis unde omnis</li><li>Ted ut perspiciatis unde omnis</li><li>Ted ut perspiciatis unde omnis</li><li>Ted ut perspiciatis unde omnis</li><li>Ted ut perspiciatis unde omnis</li></ul></div>
    <div class="link-col abs" style="left:346px"><h4>Lorum Ipsum</h4><ul><li>Ted ut perspiciatis unde omnis</li><li>Ted ut perspiciatis unde omnis</li><li>Ted ut perspiciatis unde omnis</li><li>Ted ut perspiciatis unde omnis</li><li>Ted ut perspiciatis unde omnis</li><li>Ted ut perspiciatis unde omnis</li><li>Ted ut perspiciatis unde omnis</li></ul></div>
    <div class="link-col abs" style="left:599px"><h4>Lorum Ipsum</h4><ul><li>Ted ut perspiciatis unde omnis</li><li>Ted ut perspiciatis unde omnis</li><li>Ted ut perspiciatis unde omnis</li><li>Ted ut perspiciatis unde omnis</li><li>Ted ut perspiciatis unde omnis</li><li>Ted ut perspiciatis unde omnis</li><li>Ted ut perspiciatis unde omnis</li></ul></div>
    <div class="link-col abs" style="left:851px"><h4>Lorum Ipsum</h4><ul><li>Ted ut perspiciatis unde omnis</li><li>Ted ut perspiciatis unde omnis</li><li>Ted ut perspiciatis unde omnis</li><li>Ted ut perspiciatis unde omnis</li><li>Ted ut perspiciatis unde omnis</li><li>Ted ut perspiciatis unde omnis</li><li>Ted ut perspiciatis unde omnis</li></ul></div>
  </section>

  <footer class="site-footer abs">
    <p class="copyright abs">© DURVELO, Inc. 2013</p>
    <div class="follow abs">Follow us on&nbsp;<i></i><i></i><i></i><i></i></div>
  </footer>
</body>
</html>
```